Alberta, Canada based Environmental Oilfield Consultant need a Business Card Design

We need a business card design for a year old company based in Edmonton, Alberta, Canada called Ferncrest Consulting Inc. We are environmental consultants primarily for oilfield based companies (pipeline cleanup, site consultations, environmental site training, and site evaluations).

We like the color blue or green, something very clean and crisp looking.
We don't really care if there is an otter on it but most of our work is land based and nothing really to do with oceans or larger bodies of water.

The name Ferncrest was the name of our fathers boat, and named our company that in his memory.

```html
<!DOCTYPE html>
<html lang="en">
<head>
<meta charset="utf-8">
<title>Ferncrest Consulting Inc. – Business Card</title>
<link rel="stylesheet" href="https://fonts.googleapis.com/css2?family=Source+Sans+3:wght@400;500&display=swap">
<style>
  :root {
    --backdrop: #1c1c1c;
    --sky-blue: #0aaee8;
    --deep-blue: #0a80b0;
    --white: #ffffff;
    --leaf-green: #2f7d3c;
  }
  * { margin: 0; padding: 0; box-sizing: border-box; }
  html, body {
    width: 1200px; height: 761px; overflow: hidden;
    background: var(--backdrop);
    font-family: "Source Sans 3", "Myriad Pro", sans-serif;
    color: var(--white);
  }
  .business-card {
    position: absolute; left: 322px; top: 213px;
    width: 552px; height: 331px;
    background: var(--sky-blue);
    overflow: hidden;
  }
  .card-wave { position: absolute; inset: 0; }
  .tree-art { position: absolute; left: 402px; top: 78px; }
  .company-name {
    position: absolute; left: 38px; top: 36px;
    font-size: 30px; font-weight: 400; font-variant: small-caps;
    letter-spacing: 0.3px; white-space: nowrap; line-height: 1;
  }
  .company-rule {
    position: absolute; left: 38px; top: 71px;
    width: 315px; height: 2px; background: var(--white);
  }
  .company-tagline {
    position: absolute; left: 40px; top: 73px;
    font-size: 20px; line-height: 1.2; white-space: nowrap;
  }
  .person-name {
    position: absolute; left: 38px; top: 198px;
    font-size: 35px; line-height: 1; white-space: nowrap;
  }
  .person-role {
    position: absolute; left: 39px; top: 233px;
    font-size: 22.5px; line-height: 1; white-space: nowrap;
  }
  .contact-item {
    position: absolute; display: flex; align-items: flex-start; gap: 10px;
    font-size: 16.5px; line-height: 1.25; white-space: nowrap;
  }
  .contact-item svg { flex: none; margin-top: 2px; }
  .contact-phone { left: 291px; top: 189px; }
  .contact-email { left: 274px; top: 210px; }
  .contact-web { left: 255px; top: 232px; }
  .contact-address { left: 242px; top: 255px; gap: 18px; }
</style>
</head>
<body>
  <section class="business-card">
    <svg class="card-wave" width="552" height="331" viewBox="0 0 552 331" aria-hidden="true">
      <path fill="var(--white)" d="M0,168 L270,168 C318,138 350,122 383,122 C420,122 450,188 498,188 C522,188 540,176 552,166 L552,331 L0,331 Z"/>
      <path fill="var(--deep-blue)" d="M0,180 L273,180 C320,150 350,134 383,134 C420,134 450,200 498,200 C522,200 540,189 552,179 L552,331 L0,331 Z"/>
    </svg>
    <svg class="tree-art" width="132" height="110" viewBox="0 0 132 110" role="img" aria-label="Illustration of three young white-stemmed trees with green leaves on the hill">
      <rect x="0" y="0" width="132" height="110" rx="30" fill="var(--leaf-green)"/>
    </svg>

    <h1 class="company-name">Ferncrest Consulting inc.</h1>
    <div class="company-rule"></div>
    <p class="company-tagline">Environmental Consulting</p>

    <p class="person-name">John Doe</p>
    <p class="person-role">General Manager</p>

    <p class="contact-item contact-phone">
      <svg width="16" height="16" viewBox="0 0 24 24" aria-hidden="true"><path fill="var(--white)" d="M6.6 10.8a15.1 15.1 0 0 0 6.6 6.6l2.2-2.2a1 1 0 0 1 1-.25 11.4 11.4 0 0 0 3.6.57 1 1 0 0 1 1 1V20a1 1 0 0 1-1 1A17 17 0 0 1 3 4a1 1 0 0 1 1-1h3.5a1 1 0 0 1 1 1c0 1.25.2 2.45.57 3.6a1 1 0 0 1-.25 1z"/></svg>
      <span>+1 55501 678 90</span>
    </p>
    <p class="contact-item contact-email">
      <svg width="18" height="14" viewBox="0 0 18 14" aria-hidden="true"><rect x="0" y="1" width="18" height="12" fill="var(--white)"/><path d="M0.5 1.5 L9 8 L17.5 1.5" fill="none" stroke="var(--deep-blue)" stroke-width="1.4"/></svg>
      <span>john@ferncrestconsulting.com</span>
    </p>
    <p class="contact-item contact-web">
      <svg width="17" height="17" viewBox="0 0 20 20" aria-hidden="true"><circle cx="10" cy="10" r="8.5" fill="none" stroke="var(--white)" stroke-width="2"/><ellipse cx="10" cy="10" rx="3.5" ry="8.5" fill="none" stroke="var(--white)" stroke-width="1.6"/><path d="M2 10 H18" stroke="var(--white)" stroke-width="1.6"/></svg>
      <span>www.ferncrestconsulting.com</span>
    </p>
    <p class="contact-item contact-address">
      <svg width="13" height="18" viewBox="0 0 12 18" aria-hidden="true" style="margin-top:5px"><path fill="var(--white)" d="M6 0a6 6 0 0 0-6 6c0 4.5 6 12 6 12s6-7.5 6-12a6 6 0 0 0-6-6zm0 8.3a2.3 2.3 0 1 1 0-4.6 2.3 2.3 0 0 1 0 4.6z"/></svg>
      <span>Maplegrove, Alberta, Canada<br>20480</span>
    </p>
  </section>
</body>
</html>
```